Psychology and personal development service needs an awesome Web Design

Hi, we are Bright, Steady & Kind, a psychology and personal development service located in Melbourne Australia. We already have a website www.brightsteady&kind.org but it is in great need of a makeover! We add to the website regularly with articles and so we need a space to archive these when they come off the main page, and we have products that we would like to sell internationally so we need a shop page that can convert currencies for international sales and calculate postage and handling. We have a Facebook page that we would like to link as well as a newsletter that we would like to archive on the website. We have just had a logo designed through craft huddle and would like to incorporate this into our website. We want something with high visual impact and uncluttered.
We also run workshops and events so need a tab for this.
Thanks for getting on board!

```html
<!DOCTYPE html>
<html lang="en">
<head>
<meta charset="utf-8">
<title>Bright, Steady &amp; Kind</title>
<link rel="stylesheet" href="https://fonts.googleapis.com/css2?family=Raleway:wght@500;700;800&family=Dancing+Script:wght@500;700&family=Kaushan+Script&family=EB+Garamond&family=Arimo&display=swap">
<style>
:root{
  --purple:#7e5a9b;
  --purple-band:#8a6aa6;
  --purple-box:#9c82b5;
  --teal:#6cc3c3;
  --teal-dark:#4fa8aa;
  --grey:#dcdfe0;
  --ink:#333;
  --muted:#777;
  --white:#fff;
}
*{margin:0;padding:0;box-sizing:border-box}
html,body{width:695px;height:1200px;overflow:hidden;background:var(--white)}
body{position:relative;font-family:'Arimo',Arial,sans-serif;color:var(--ink)}
.abs{position:absolute}

/* header */
.site-header{position:absolute;left:0;top:0;width:695px;height:67px;background:var(--white)}
.brand{left:130px;top:12px;display:flex;align-items:center;gap:7px}
.brand-dot{width:26px;height:26px;border-radius:50%;background:var(--purple);flex:none}
.brand-name{font-family:'Raleway',sans-serif;font-weight:700;font-size:14px;line-height:15px;color:var(--purple);width:70px}
.call{left:408px;top:17px;font-size:7px;letter-spacing:.2px;white-space:nowrap;color:var(--purple)}
.social{left:514px;top:14px;display:flex;gap:3px}
.social span{width:10px;height:10px;border-radius:50%;background:#a6a6a6}
.nav{left:248px;top:39px;display:flex;gap:19px;font-family:'Raleway',sans-serif;font-weight:700;font-size:9px;letter-spacing:.4px;color:#222}
.nav-wave{left:248px;top:51px}

/* hero */
.hero{position:absolute;left:0;top:67px;width:695px;height:220px;overflow:hidden}
.hero-art{position:absolute;inset:0;background:linear-gradient(100deg,#7fcdcc 0%,#6cc1c2 50%,#5fb6b7 100%)}
.hero-figure{position:absolute;left:385px;top:10px;width:170px;height:200px;background:radial-gradient(ellipse at 50% 60%,#4a9fa2 0%,rgba(74,159,162,0) 70%)}
.hero-script{left:138px;top:85px;font-family:'Dancing Script',cursive;font-weight:700;font-size:21px;color:var(--white);transform:rotate(-4deg)}
.hero-title{left:138px;top:108px;font-family:'Raleway',sans-serif;font-weight:800;font-size:29px;line-height:27px;color:var(--white)}
.hero-title em{font-style:normal;color:var(--purple)}
.hero-quote{left:398px;top:50px;width:80px;font-family:'EB Garamond',serif;font-size:6.5px;line-height:9px;color:var(--white)}
.peace{position:absolute;left:0;top:207px;width:695px;height:13px;display:flex;gap:10px;white-space:nowrap;font-family:'Raleway',sans-serif;font-weight:500;font-size:11px;letter-spacing:1px;color:rgba(255,255,255,.75);line-height:13px;margin-left:-18px}
.peace svg{flex:none;margin-top:3px}

/* section headings */
.section-title{display:flex;align-items:center;gap:6px;font-family:'Raleway',sans-serif;font-weight:700;font-size:12px;letter-spacing:.3px}

/* features */
.features{position:absolute;left:0;top:287px;width:695px;height:423px;background:var(--grey)}
.features .section-title{left:139px;top:23px;color:#666}
.feature .num{font-family:'Kaushan Script',cursive;font-size:50px;line-height:50px}
.feature .art{position:absolute;width:98px;height:98px;border-radius:50%}
.feature .tag{position:absolute;font-family:'Dancing Script',cursive;font-size:11px;color:#777;white-space:nowrap}
.feature .name{position:absolute;font-family:'Raleway',sans-serif;font-weight:800;font-size:20px;line-height:20px;text-align:center;white-space:nowrap}
.is-purple{color:var(--purple)}
.is-teal{color:var(--teal)}
.art-purple{background:radial-gradient(circle at 50% 60%,#b9a8cb 0%,var(--purple) 65%)}
.art-teal{background:radial-gradient(circle at 50% 55%,#bfe6e5 0%,var(--teal) 65%)}

/* reviews */
.reviews{position:absolute;left:0;top:710px;width:695px;height:205px;background:var(--white)}
.reviews .section-title{left:139px;top:23px;color:#888}
.review{position:absolute;width:180px}
.review .mark{position:absolute;left:0;top:-2px;width:28px;height:22px;border-left:9px solid #c9e9e8;border-right:9px solid #c9e9e8}
.review h3{position:relative;font-family:'Raleway',sans-serif;font-weight:800;font-size:14px;color:var(--purple);letter-spacing:.3px}
.review p{margin-top:6px;font-family:'EB Garamond',serif;font-size:7.8px;line-height:10px;color:#222}
.review .by{margin-top:12px;font-size:6.5px;color:var(--teal-dark)}

/* gallery */
.gallery{position:absolute;left:0;top:915px;width:695px;height:116px;background:var(--purple-band)}
.gallery .section-title{left:139px;top:10px;color:var(--white)}
.thumb{position:absolute;top:37px;width:88px;height:63px;background:var(--purple-box)}

/* footer */
.footer{position:absolute;left:0;top:1031px;width:695px;height:169px;background:var(--white)}
.links{position:absolute;top:22px;list-style:none;font-size:6.8px;line-height:10.4px;color:#444}
.address{left:375px;top:28px;font-size:6.8px;line-height:10px;color:#444}
.address .label{color:var(--purple)}
.address .cta{margin-top:3px;font-size:8.5px;letter-spacing:.3px;color:#222}
.btn{left:375px;top:97px;width:105px;height:25px;border-radius:13px;background:var(--teal);color:var(--white);font-size:8.5px;line-height:25px;text-align:center;letter-spacing:.4px}
.legal{top:151px;font-size:5.8px;color:#444}
</style>
</head>
<body>

<header class="site-header">
  <div class="abs brand"><span class="brand-dot"></span><span class="brand-name">Bright, Steady &amp; Kind</span></div>
  <div class="abs call">CALL US ON 180 555 0142</div>
  <div class="abs social"><span></span><span></span><span></span><span></span></div>
  <nav class="abs nav"><span>HOME</span><span>ABOUT US</span><span>PRODUCTS</span><span>SERVICES</span><span>CLIENTS</span><span>CONTACT US</span></nav>
  <svg class="abs nav-wave" width="22" height="8" viewBox="0 0 22 8"><path d="M1 2q2.5-2 5 0t5 0 5 0 5 0M1 6q2.5-2 5 0t5 0 5 0 5 0" fill="none" stroke="#7e5a9b" stroke-width="1.2"/></svg>
</header>

<section class="hero">
  <div class="hero-art" role="img" aria-label="Soft teal scene with a tree, a woman meditating in a lotus pose and a bird by the water"></div>
  <div class="hero-figure"></div>
  <div class="abs hero-script">Teach how to to live</div>
  <h1 class="abs hero-title">HOW <em>LIFE</em> WILL<br>GOING HAPPY</h1>
  <p class="abs hero-quote">We sat with you in really difficult situations in Melbourne<br><br>by Ana</p>
  <div class="peace">
    <span>FIND PEACE</span><svg width="14" height="7" viewBox="0 0 14 7"><path d="M1 2q1.5-2 3 0t3 0 3 0 3 0M1 5.5q1.5-2 3 0t3 0 3 0 3 0" fill="none" stroke="#fff" stroke-opacity=".75"/></svg>
    <span>FIND PEACE</span><svg width="14" height="7" viewBox="0 0 14 7"><path d="M1 2q1.5-2 3 0t3 0 3 0 3 0M1 5.5q1.5-2 3 0t3 0 3 0 3 0" fill="none" stroke="#fff" stroke-opacity=".75"/></svg>
    <span>FIND PEACE</span><svg width="14" height="7" viewBox="0 0 14 7"><path d="M1 2q1.5-2 3 0t3 0 3 0 3 0M1 5.5q1.5-2 3 0t3 0 3 0 3 0" fill="none" stroke="#fff" stroke-opacity=".75"/></svg>
    <span>FIND PEACE</span><svg width="14" height="7" viewBox="0 0 14 7"><path d="M1 2q1.5-2 3 0t3 0 3 0 3 0M1 5.5q1.5-2 3 0t3 0 3 0 3 0" fill="none" stroke="#fff" stroke-opacity=".75"/></svg>
    <span>FIND PEACE</span><svg width="14" height="7" viewBox="0 0 14 7"><path d="M1 2q1.5-2 3 0t3 0 3 0 3 0M1 5.5q1.5-2 3 0t3 0 3 0 3 0" fill="none" stroke="#fff" stroke-opacity=".75"/></svg>
    <span>FIND PEACE</span><svg width="14" height="7" viewBox="0 0 14 7"><path d="M1 2q1.5-2 3 0t3 0 3 0 3 0M1 5.5q1.5-2 3 0t3 0 3 0 3 0" fill="none" stroke="#fff" stroke-opacity=".75"/></svg>
    <span>FIND PEACE</span><svg width="14" height="7" viewBox="0 0 14 7"><path d="M1 2q1.5-2 3 0t3 0 3 0 3 0M1 5.5q1.5-2 3 0t3 0 3 0 3 0" fill="none" stroke="#fff" stroke-opacity=".75"/></svg>
    <span>FIND PEACE</span>
  </div>
</section>

<section class="features">
  <h2 class="abs section-title"><svg width="20" height="8" viewBox="0 0 20 8"><path d="M1 2q2.25-2 4.5 0t4.5 0 4.5 0 4.5 0M1 6q2.25-2 4.5 0t4.5 0 4.5 0 4.5 0" fill="none" stroke="#7e5a9b" stroke-width="1.2"/></svg>FEATURES SERVICES</h2>

  <div class="feature">
    <span class="abs num is-purple" style="left:160px;top:52px">1</span>
    <div class="art art-purple" style="left:208px;top:52px" role="img" aria-label="Purple brush circle with a standing figure silhouette"></div>
    <span class="tag" style="left:188px;top:156px">To Boost your confidence</span>
    <span class="name is-purple" style="left:176px;top:170px">DURING YOUR<br>PRESENTATION</span>
  </div>
  <div class="feature">
    <span class="abs num is-teal" style="left:356px;top:52px">2</span>
    <div class="art art-teal" style="left:415px;top:52px" role="img" aria-label="Teal brush circle with smiling lips"></div>
    <span class="tag" style="left:392px;top:156px">To Make your Audience</span>
    <span class="name is-teal" style="left:386px;top:170px">CONFORTABLE<br>SIMPLY SMILE</span>
  </div>
  <div class="feature">
    <span class="abs num is-teal" style="left:160px;top:234px">3</span>
    <div class="art art-teal" style="left:208px;top:235px" role="img" aria-label="Teal brush circle with a figure in a yoga backbend"></div>
    <span class="tag" style="left:182px;top:336px">To Engage People, Gestures</span>
    <span class="name is-teal" style="left:160px;top:352px">WITH YOUR<br>ARMS AND HANDS</span>
  </div>
  <div class="feature">
    <span class="abs num is-purple" style="left:356px;top:234px">4</span>
    <div class="art art-purple" style="left:415px;top:235px" role="img" aria-label="Purple brush circle with footprints"></div>
    <span class="tag" style="left:408px;top:336px">Bring Movment your</span>
    <span class="name is-purple" style="left:386px;top:352px">SPEECH USE THE<br>PHYSICAL SPACE</span>
  </div>
</section>

<section class="reviews">
  <h2 class="abs section-title"><svg width="20" height="8" viewBox="0 0 20 8"><path d="M1 2q2.25-2 4.5 0t4.5 0 4.5 0 4.5 0M1 6q2.25-2 4.5 0t4.5 0 4.5 0 4.5 0" fill="none" stroke="#7e5a9b" stroke-width="1.2"/></svg>CLIENT REVIEW</h2>
  <article class="review" style="left:160px;top:74px">
    <span class="mark"></span>
    <h3>CONSECTETUR</h3>
    <p>habitasse platea dictumst. Nunc varius lorem libero, at feugiat urna facilisis nec. Etiam felis neque, viverra quis turpis ac, tempus laoreet quam.</p>
    <p class="by">by Fluxus</p>
  </article>
  <article class="review" style="left:360px;top:74px">
    <span class="mark"></span>
    <h3>CONSECTETUR</h3>
    <p>habitasse platea dictumst. Nunc varius lorem libero, at feugiat urna facilisis nec. Etiam felis neque, viverra quis turpis ac, tempus laoreet quam.</p>
    <p class="by">by Fluxus</p>
  </article>
</section>

<section class="gallery">
  <h2 class="abs section-title"><svg width="20" height="8" viewBox="0 0 20 8"><path d="M1 2q2.25-2 4.5 0t4.5 0 4.5 0 4.5 0M1 6q2.25-2 4.5 0t4.5 0 4.5 0 4.5 0" fill="none" stroke="#fff" stroke-width="1.2"/></svg>IMAGE GALLARY</h2>
  <div class="thumb" style="left:163px"></div>
  <div class="thumb" style="left:257px"></div>
  <div class="thumb" style="left:351px"></div>
  <div class="thumb" style="left:444px"></div>
</section>

<footer class="footer">
  <ul class="links" style="left:139px">
    <li>Home</li><li>Welcome</li><li>About us</li><li>Books</li><li>Online Store</li><li>Contact us</li><li>Body Talk</li><li>Relationships</li><li>Parents &amp; children</li>
  </ul>
  <ul class="links" style="left:235px">
    <li>Transforming</li><li>Discover Self Worth</li><li>I Don't have Time</li><li>Parasites</li><li>Sufing</li><li>Create A Legency</li><li>Miscellaneous</li><li>Technology</li><li>Success</li>
  </ul>
  <div class="abs address">
    <div class="label">Address</div>
    <div>2210 Harbour Lane,</div>
    <div>Fitzroy VIC 3065</div>
    <div>Tel: 03-9000-4127</div>
    <div class="cta">LET'S DISCUSS YOUR MARKETING NEEDS TODAY.</div>
  </div>
  <div class="abs btn">CONTACT US</div>
  <div class="abs legal" style="left:128px">© Copyright 2013 brightsteadyandkind.org. All Rights Reserved.</div>
  <div class="abs legal" style="left:439px">Designed and Developed by Northpeakstudio.com</div>
</footer>

</body>
</html>
```